Copperleaf Motorized Shade Business Card

Hello, we've had our logo made. Now we are looking for a clean and cool looking business card. One side can just be the logo with any design elements that might look good with it. The other side will be Name, Phone Number and Email. There will not be an address on the card.

```html
<!DOCTYPE html>
<html lang="en">
<head>
<meta charset="utf-8">
<title>Copperleaf Motorized Shades – Business Card</title>
<link href="https://fonts.googleapis.com/css2?family=Archivo:wght@700&family=Questrial&display=swap" rel="stylesheet">
<style>
  :root {
    --bg: #e9e9e7;
    --navy: #1f4a7f;
    --navy-dark: #173c6b;
    --sky: #2aa1d8;
    --sun: #f2c230;
    --paper: #f7f7f5;
    --ink: #2b2b2b;
    --white: #ffffff;
  }
  * { margin: 0; padding: 0; box-sizing: border-box; }
  html, body {
    width: 1200px; height: 801px; overflow: hidden;
    background: var(--bg);
    font-family: "Questrial", Arial, sans-serif;
  }
  .stage {
    position: relative; width: 1200px; height: 801px;
  }
  .card {
    position: absolute;
    width: 520px; height: 297px;
    border-bottom: 4px solid var(--sun);
    border-right: 3px solid var(--sun);
    box-shadow: 0 6px 18px rgba(0,0,0,.12);
  }
  /* Front side */
  .card-front {
    left: 70px; top: 110px;
    background: var(--navy);
    display: flex; align-items: center; justify-content: center;
  }
  .brand {
    display: flex; align-items: center; gap: 14px;
  }
  .brand-mark {
    width: 22px; height: 22px; background: var(--sun);
  }
  .brand-name {
    font-family: "Questrial", Arial, sans-serif;
    font-size: 30px; letter-spacing: 2px; line-height: 1.05;
    text-transform: uppercase;
  }
  .brand-name small {
    display: block; font-size: 14px; letter-spacing: 4px;
  }
  .card-front .brand-name { color: var(--white); }

  /* Back side */
  .card-back {
    left: 610px; top: 394px;
    background: var(--paper);
  }
  .card-back .brand {
    position: absolute; top: 40px; right: 36px;
  }
  .card-back .brand-name { color: var(--navy); font-size: 26px; }
  .card-back .brand-name small { font-size: 12px; }
  .person {
    position: absolute; left: 36px; top: 150px;
  }
  .person-name {
    font-family: "Archivo", Arial, sans-serif; font-weight: 700;
    font-size: 20px; color: var(--navy-dark); text-transform: uppercase;
  }
  .person-role {
    font-size: 16px; color: var(--ink); margin-top: 2px;
  }
  .contacts {
    list-style: none; margin-top: 16px;
  }
  .contacts li {
    display: flex; align-items: center; gap: 10px;
    font-size: 14px; color: var(--ink); margin-bottom: 5px;
  }
  .contacts svg { width: 13px; height: 13px; fill: var(--navy); flex: none; }
</style>
</head>
<body>
<main class="stage">
  <section class="card card-front">
    <div class="brand">
      <span class="brand-mark"></span>
      <p class="brand-name">Copperleaf<small>Motorized Shades</small></p>
    </div>
  </section>

  <section class="card card-back">
    <div class="brand">
      <span class="brand-mark"></span>
      <p class="brand-name">Copperleaf<small>Motorized Shades</small></p>
    </div>
    <div class="person">
      <h1 class="person-name">Dana Whitlow</h1>
      <p class="person-role">Director</p>
      <ul class="contacts">
        <li>
          <svg viewBox="0 0 24 24" aria-hidden="true"><path d="M6.6 10.8a15 15 0 0 0 6.6 6.6l2.2-2.2a1 1 0 0 1 1-.25 11.4 11.4 0 0 0 3.6.6 1 1 0 0 1 1 1V20a1 1 0 0 1-1 1A17 17 0 0 1 3 4a1 1 0 0 1 1-1h3.5a1 1 0 0 1 1 1c0 1.25.2 2.45.6 3.6a1 1 0 0 1-.25 1z"/></svg>
          555 014 2288
        </li>
        <li>
          <svg viewBox="0 0 24 24" aria-hidden="true"><path d="M2 5h20v14H2z M2 5l10 7 10-7" /></svg>
          info@copperleafshades.com
        </li>
        <li>
          <svg viewBox="0 0 24 24" aria-hidden="true"><circle cx="12" cy="12" r="10"/></svg>
          www.copperleafshades.com
        </li>
      </ul>
    </div>
  </section>
</main>
</body>
</html>
```